Business card for apparel company. Specializing in fishing and boating performance wear. Main company name is Marlow Pelican Company, LLC brand name for apparel is TIDEWAKE. See website www.TidewakeBayline.com I will attach some logos to consider.

```html
<!DOCTYPE html>
<html lang="en">
<head>
<meta charset="utf-8">
<title>Tidewake Business Card</title>
<link href="https://fonts.googleapis.com/css2?family=Figtree:wght@400;800&display=swap" rel="stylesheet">
<style>
  :root {
    --page-bg: #e9e9ea;
    --card-white: #ffffff;
    --blue-light: #1ea8e2;
    --blue-deep: #3566b8;
    --brand-blue: #2a8fd8;
    --badge-slate: #3f4a57;
    --badge-sea: #a8cbc6;
    --text-on-blue: #ffffff;
  }
  * { box-sizing: border-box; margin: 0; padding: 0; }
  html, body {
    width: 1160px; height: 1200px; overflow: hidden;
    background: var(--page-bg);
    font-family: "Figtree", Arial, sans-serif;
  }
  .canvas { position: relative; width: 1160px; height: 1200px; }
  .card {
    position: absolute; left: 191px; width: 778px; height: 442px;
    border-radius: 30px; overflow: hidden;
    box-shadow: 0 14px 30px rgba(0,0,0,0.18);
  }
  .card-front { top: 104px; background: var(--card-white); }
  .card-back {
    top: 634px;
    background: linear-gradient(90deg, var(--blue-light) 0%, var(--blue-deep) 100%);
  }
  .brand-lockup {
    position: absolute; display: flex; align-items: center; gap: 10px;
    font-weight: 800; letter-spacing: 1px;
  }
  .front-lockup { left: 70px; top: 142px; color: var(--brand-blue); font-size: 34px; }
  .brand-dot { width: 16px; height: 16px; border-radius: 50%; background: currentColor; }
  .badge { position: absolute; border-radius: 50%; }
  .badge-original {
    left: 331px; top: 95px; width: 140px; height: 140px;
    background: radial-gradient(circle, #ffffff 0 52%, var(--badge-slate) 53% 100%);
  }
  .badge-local {
    left: 530px; top: 101px; width: 140px; height: 140px;
    background: radial-gradient(circle, #ffffff 0 45%, var(--badge-sea) 46% 80%, var(--badge-slate) 81% 100%);
  }
  .contact-band {
    position: absolute; left: 0; top: 320px; width: 100%; height: 78px;
    background: linear-gradient(90deg, var(--blue-light) 0%, var(--blue-deep) 100%);
    color: var(--text-on-blue); font-size: 19.5px; font-weight: 400;
  }
  .company-block {
    position: absolute; right: 386px; top: 12px; text-align: right; line-height: 31px;
  }
  .band-divider {
    position: absolute; left: 409px; top: 17px; width: 2px; height: 50px;
    background: var(--text-on-blue);
  }
  .online-block { position: absolute; left: 425px; top: 12px; line-height: 31px; }
  .online-row { display: flex; align-items: center; gap: 14px; }
  .online-row svg { width: 20px; height: 20px; flex: none; }
  .back-lockup {
    left: 0; right: 0; top: 190px; justify-content: center;
    color: var(--text-on-blue); font-size: 64px; letter-spacing: 2px;
  }
  .back-lockup .brand-dot { width: 26px; height: 26px; }
</style>
</head>
<body>
<main class="canvas">
  <section class="card card-front">
    <div class="brand-lockup front-lockup"><span class="brand-dot"></span>TIDEWAKE</div>
    <div class="badge badge-original" role="img" aria-label="Round brand badge, slate ring"></div>
    <div class="badge badge-local" role="img" aria-label="Round brand badge with sea-green fish emblem"></div>
    <div class="contact-band">
      <div class="company-block">
        <p>Marlow Pelican Company, LLC</p>
        <p>P.O. Box 418 Marlow, Florida 34512</p>
      </div>
      <div class="band-divider"></div>
      <div class="online-block">
        <p class="online-row">
          <svg viewBox="0 0 20 20" aria-hidden="true"><rect x="1" y="4" width="18" height="12" fill="#fff"/><path d="M1 4 L10 11 L19 4" fill="none" stroke="#2a7fcc" stroke-width="1.6"/></svg>
          info@MarlowPelicanCo.com
        </p>
        <p class="online-row">
          <svg viewBox="0 0 20 20" aria-hidden="true"><circle cx="10" cy="10" r="8.5" fill="#fff"/><path d="M5 6 Q8 5 9 8 Q7 11 9 14 M12 4 Q14 8 12 10 Q14 13 15 15" fill="none" stroke="#2a7fcc" stroke-width="1.6"/></svg>
          www.TidewakeBayline.com
        </p>
      </div>
    </div>
  </section>
  <section class="card card-back">
    <div class="brand-lockup back-lockup"><span class="brand-dot"></span>TIDEWAKE</div>
  </section>
</main>
</body>
</html>
```